" Entregamos soluções corporativas com excelência no que se refere ao capital humano e comunicação, estreitando laços de confiança com nossos clientes e proporcionando experiências de sucesso. Realizamos todo o processo de seleção, treinamento e coaching de acordo com as necessidades dos nossos clientes. "

```html
<!DOCTYPE html>
<html lang="pt-BR">
<head>
<meta charset="utf-8">
<title>Vértice – Cartão de visita</title>
<link href="https://fonts.googleapis.com/css2?family=Roboto:wght@400;500;700&family=Roboto+Condensed:wght@400&display=swap" rel="stylesheet">
<style>
  :root {
    --navy: #0f1d4a;
    --sky: #5a8fce;
    --paper: #ffffff;
    --ink: #1e2230;
    --muted: #4a4f5c;
    --backdrop: #e8e5e0;
  }
  * { margin: 0; padding: 0; box-sizing: border-box; }
  html, body { width: 1200px; height: 1200px; overflow: hidden; }
  body {
    background: var(--backdrop);
    position: relative;
    font-family: "Roboto", Arial, sans-serif;
  }
  .card {
    position: absolute;
    left: 257px;
    width: 684px;
    height: 384px;
    box-shadow: 0 6px 18px rgba(0,0,0,0.18);
  }
  .card--front {
    top: 163px;
    background: var(--navy);
    display: flex;
    flex-direction: column;
    align-items: center;
    justify-content: center;
    padding-top: 40px;
  }
  .wordmark {
    display: flex;
    align-items: center;
    gap: 18px;
  }
  .wordmark__dot {
    width: 26px; height: 26px; border-radius: 50%;
    background: var(--sky);
  }
  .wordmark__name {
    font-weight: 700;
    font-size: 84px;
    letter-spacing: 3px;
    color: var(--paper);
    line-height: 1;
  }
  .tagline {
    margin-top: 10px;
    font-family: "Roboto", Arial, sans-serif;
    font-weight: 500;
    font-size: 17px;
    letter-spacing: 5px;
    color: var(--sky);
    text-transform: uppercase;
  }
  .card--back {
    top: 648px;
    background: var(--paper);
  }
  .card--back .wordmark {
    position: absolute;
    left: 58px;
    top: 168px;
    gap: 10px;
  }
  .card--back .wordmark__dot { width: 16px; height: 16px; }
  .card--back .wordmark__name {
    color: var(--navy);
    font-size: 36px;
    letter-spacing: 1px;
  }
  .divider {
    position: absolute;
    left: 271px;
    top: 115px;
    width: 3px;
    height: 160px;
    background: var(--navy);
  }
  .contact {
    position: absolute;
    left: 298px;
    top: 118px;
  }
  .contact__name {
    font-weight: 500;
    font-size: 28px;
    color: var(--ink);
    line-height: 1.1;
  }
  .contact__role {
    font-family: "Roboto Condensed", Arial, sans-serif;
    font-size: 20px;
    color: var(--muted);
    margin-top: 4px;
    margin-bottom: 14px;
  }
  .contact__line {
    display: flex;
    align-items: center;
    gap: 12px;
    font-family: "Roboto Condensed", Arial, sans-serif;
    font-size: 20px;
    color: var(--ink);
    height: 36px;
  }
  .contact__icon { width: 26px; height: 26px; flex: none; }
  .band {
    position: absolute;
    right: 0;
    top: 53px;
    width: 77px;
    height: 283px;
    background: var(--navy);
  }
</style>
</head>
<body>
  <section class="card card--front">
    <div class="wordmark">
      <span class="wordmark__dot"></span>
      <span class="wordmark__name">VÉRTICE</span>
    </div>
    <p class="tagline">Soluções Corporativas</p>
  </section>

  <section class="card card--back">
    <div class="wordmark">
      <span class="wordmark__dot"></span>
      <span class="wordmark__name">VÉRTICE</span>
    </div>
    <div class="divider"></div>
    <div class="contact">
      <p class="contact__name">Renata Moreira</p>
      <p class="contact__role">Cargo</p>
      <p class="contact__line">
        <svg class="contact__icon" viewBox="0 0 26 26"><rect width="26" height="26" rx="5" fill="#5a8fce"/><path d="M8 6c1-1 2 0 3 2s0 2-1 3c1 2 3 4 5 5 1-1 1-2 3-1s3 2 2 3c-1 2-3 3-6 1-3-2-5-4-7-7-1-3 0-5 1-6z" fill="#fff"/></svg>
        (00) 0000-0000
      </p>
      <p class="contact__line">
        <svg class="contact__icon" viewBox="0 0 26 26"><rect width="26" height="26" rx="5" fill="#5a8fce"/><rect x="5" y="8" width="16" height="11" rx="1" fill="#fff"/><path d="M5 8l8 6 8-6" stroke="#5a8fce" stroke-width="1.5" fill="none"/></svg>
        contato@vertice.com.br
      </p>
      <p class="contact__line">
        <svg class="contact__icon" viewBox="0 0 26 26"><rect width="26" height="26" rx="5" fill="#5a8fce"/><circle cx="13" cy="13" r="7.5" fill="none" stroke="#fff" stroke-width="1.6"/><ellipse cx="13" cy="13" rx="3.2" ry="7.5" fill="none" stroke="#fff" stroke-width="1.4"/><path d="M5.5 13h15" stroke="#fff" stroke-width="1.4"/></svg>
        www.vertice.com.br
      </p>
    </div>
    <div class="band"></div>
  </section>
</body>
</html>
```